Washing Up Liquid Label

We are looking for 2 labels to be designed to be part of a range of products.

The brand is Velmora Max and we are looking for a label design to you on washing up liquid bottle similar to the ones in the file attached.

One label it be original and the liquid will be green so the label colour needs to be green or work with the green. The other label is lemon and is yellow.

Please see attached the Velmora Max logo and also a couple of the other designs in the range.

```html
<!DOCTYPE html>
<html lang="en">
<head>
<meta charset="utf-8">
<title>Velmora Max – Washing Up Liquid Labels</title>
<link href="https://fonts.googleapis.com/css2?family=Ubuntu:ital,wght@0,400;0,500;0,700;1,500&family=Arimo:wght@400;700&display=swap" rel="stylesheet">
<style>
  :root {
    --page: #ffffff;
    --panel-light: #3f8a4a;
    --panel-dark: #0f6235;
    --lemon: #fff200;
    --lemon-soft: #fffbc8;
    --leaf: #2f9a3a;
    --leaf-soft: #e4f4e4;
    --centre: #ffffff;
    --navy: #14358a;
    --accent-green: #8ab61d;
    --ink: #2b2b2b;
    --badge: #e5531a;
    --badge-text: #ffffff;
    --lemon-label: #e2641a;
    --original-label: #6fb02a;
    --small-green: #9cc21f;
  }
  * { margin: 0; padding: 0; box-sizing: border-box; }
  html, body { width: 1200px; height: 848px; overflow: hidden; background: var(--page); }
  .canvas { position: relative; width: 1200px; height: 848px; font-family: "Ubuntu", sans-serif; }
  .backdrop {
    position: absolute; left: 63px; top: 232px; width: 1067px; height: 616px;
    background: linear-gradient(135deg, var(--panel-light) 0%, var(--panel-dark) 100%);
  }
  .label { position: absolute; top: 290px; width: 484px; height: 484px; border-radius: 50%; }
  .label--lemon {
    left: 91px;
    background: radial-gradient(circle at 50% 50%, var(--centre) 0%, var(--centre) 30%, var(--lemon-soft) 55%, var(--lemon) 100%);
  }
  .label--original {
    left: 623px;
    background: radial-gradient(circle at 50% 50%, var(--centre) 0%, var(--centre) 28%, var(--leaf-soft) 50%, var(--leaf) 100%);
  }
  .badge {
    position: absolute; left: 263px; top: 28px; width: 64px; height: 40px;
    background: var(--badge); color: var(--badge-text); border-radius: 12px 12px 12px 4px;
    font: 500 13px/15px "Ubuntu", sans-serif; text-align: center; padding-top: 5px;
  }
  .tagline {
    position: absolute; left: 0; right: 0; top: 68px; text-align: center; padding-left: 118px;
    font: 500 22px/26px "Ubuntu", sans-serif; letter-spacing: -0.3px;
  }
  .label--lemon .tagline { color: var(--accent-green); }
  .label--original .tagline { color: var(--ink); }
  .brand {
    position: absolute; left: 0; right: 0; top: 170px; text-align: center;
    font: 700 66px/64px "Ubuntu", sans-serif; color: var(--navy); letter-spacing: 1px;
  }
  .brand__line { display: block; }
  .company {
    position: absolute; left: 55px; top: 355px; font: 400 11px/13px "Arimo", sans-serif;
  }
  .company span { display: block; }
  .company span + span { padding-left: 10px; }
  .company span:last-child { padding-left: 18px; }
  .label--lemon .company { color: var(--small-green); }
  .label--original .company { color: var(--ink); }
  .contents {
    position: absolute; left: 325px; top: 355px; width: 120px; text-align: center;
    font: italic 500 13px/16px "Ubuntu", sans-serif;
  }
  .contents__weight { display: block; font-size: 17px; line-height: 20px; }
  .label--lemon .contents { color: var(--accent-green); }
  .label--original .contents { color: var(--ink); }
  .flavour-art { position: absolute; left: 195px; top: 325px; width: 92px; height: 68px; border-radius: 40%; }
  .label--lemon .flavour-art { background: radial-gradient(circle at 40% 45%, #ffd21a, #f2b705 60%, rgba(120,170,60,0.6)); }
  .label--original .flavour-art { background: radial-gradient(circle at 50% 50%, rgba(255,255,255,0.9), rgba(210,240,210,0.6) 60%, rgba(255,255,255,0)); }
  .flavour {
    position: absolute; left: 0; right: 0; top: 398px; text-align: center; padding-left: 6px;
    font: 700 14px/16px "Arimo", sans-serif;
  }
  .label--lemon .flavour { color: var(--lemon-label); }
  .label--original .flavour { color: var(--original-label); }
</style>
</head>
<body>
<div class="canvas">
  <div class="backdrop"></div>

  <section class="label label--lemon">
    <div class="badge">POWER<br>TABS</div>
    <p class="tagline">For Cleaner Dishes</p>
    <h2 class="brand"><span class="brand__line">Velmora</span><span class="brand__line">Max</span></h2>
    <p class="company"><span>Velmora Home Ltd.</span><span>www.velmora-home.co.uk</span><span>telephone:01632 960418</span></p>
    <div class="flavour-art" role="img" aria-label="Illustration of a whole lemon and a lemon half with leaves"></div>
    <p class="contents">Average 40 Tablets<span class="contents__weight">800g</span></p>
    <p class="flavour">Lemon</p>
  </section>

  <section class="label label--original">
    <div class="badge">POWER<br>TABS</div>
    <p class="tagline">For Cleaner Dishes</p>
    <h2 class="brand"><span class="brand__line">Velmora</span><span class="brand__line">Max</span></h2>
    <p class="company"><span>Velmora Home Ltd.</span><span>www.velmora-home.co.uk</span><span>telephone:01632 960418</span></p>
    <div class="flavour-art" role="img" aria-label="Illustration of clear soap bubbles"></div>
    <p class="contents">Average 40 Tablets<span class="contents__weight">800g</span></p>
    <p class="flavour">Original</p>
  </section>
</div>
</body>
</html>
```